Präsentationsvorlagen für die Cloud-Plattform DataHarbor
Zielgruppe
Ich bin ein unabhängiger Berater für die Cloud-Plattform DataHarbor. Zielgruppe sind Unternehmen jeglicher Größe. Das Design sollte schlicht und aufgeräumt sein.
Aufgabenstellung
Dunkler Hintergrund und die Farben aus dem Logo sollten enthalten sein.

```html
<!DOCTYPE html>
<html lang="de">
<head>
<meta charset="utf-8">
<title>Kaltwerk – Präsentationsvorlagen</title>
<link rel="stylesheet" href="https://fonts.googleapis.com/css2?family=Mulish:ital,wght@0,400;0,600;0,700;0,800;1,400&display=swap">
<style>
:root{
  --page:#ffffff;
  --slide:#2b2b2b;
  --slide-deep:#222222;
  --orange:#e5782a;
  --blue:#3b8ed4;
  --text:#d6d6d6;
  --muted:#9a9a9a;
  --line:#555555;
}
*{box-sizing:border-box;margin:0;padding:0}
html,body{width:1200px;height:3599px;overflow:hidden;background:var(--page);font-family:"Mulish",Arial,sans-serif}
.canvas{position:relative;width:1200px;height:3599px}
.slide{position:absolute;width:519px;height:290px;background:var(--slide);overflow:hidden;box-shadow:0 2px 8px rgba(0,0,0,.15)}
.slide.light{background:#fff}
.col-left{left:64px}.col-right{left:626px}
.row1{top:904px}.row2{top:1241px}.row3{top:1577px}.row4{top:1913px}
.row5{top:2249px}.row6{top:2584px}.row7{top:2921px}.row8{top:3256px}
.brand{position:absolute;top:22px;right:14px;font-size:10px;font-weight:700;color:var(--blue);letter-spacing:.2px;display:flex;align-items:center;gap:4px}
.brand::before{content:"";width:6px;height:6px;border-radius:50%;background:var(--orange)}
.slide-title{position:absolute;font-size:20px;font-weight:600;color:#fff;text-transform:uppercase;border-left:2px solid var(--orange);padding-left:8px;line-height:1.15;letter-spacing:.3px}
.slide.light .slide-title{color:#2b2b2b}
.accent{color:var(--orange)}
.body{position:absolute;font-size:5.6px;line-height:1.7;color:var(--text)}
.body h4{font-size:6px;color:var(--orange);font-weight:700;margin-bottom:5px}
.body p+h4{margin-top:12px}
.body p+p{margin-top:8px}
.footer-note{position:absolute;left:26px;bottom:20px;font-size:5.5px;color:var(--muted)}
.page-no{position:absolute;right:26px;bottom:18px;font-size:7.5px;color:var(--muted);border-left:1px solid var(--orange);padding-left:4px}
.photo{position:absolute}
.gray-photo{background:linear-gradient(160deg,#5a5a5a 0%,#3a3a3a 55%,#262626 100%)}
.cards{position:absolute;top:78px;left:46px;display:flex;gap:23px}
.card{width:122px;height:144px;padding:8px 9px;font-size:4.4px;line-height:1.6;color:var(--text);position:relative}
.card.filled{background:#2b2b2b}
.card.outlined{border:1px solid #bdbdbd}
.card-head{display:flex;gap:6px;align-items:center;margin-bottom:8px}
.card-head svg{flex:none}
.card-title{font-size:5.2px;font-weight:700;color:#fff;line-height:1.35}
.card-title .accent{display:block}
.card-title small{display:block;color:var(--orange);font-weight:400;font-size:4.4px}
.card-duration{position:absolute;right:9px;bottom:8px}
.band{position:absolute;left:0;right:0;bottom:0;height:41px}
.band .footer-note,.band .page-no{bottom:15px}
.band.orange .footer-note,.band.orange .page-no{color:#2b2b2b;border-color:#2b2b2b}
.quote-text{position:absolute;left:56px;top:90px;font-size:14px;font-style:italic;color:#fff;line-height:1.6}
.quote-mark{position:absolute;left:40px;top:72px;font-size:54px;line-height:1;color:#8a5a30;font-weight:800}
.quote-author{position:absolute;right:50px;top:158px;font-size:8px;font-style:italic;color:#fff}
.contact{position:absolute;left:45px;top:90px;font-size:7.5px;color:#fff;width:160px}
.contact p{padding:9px 0;border-bottom:1px solid var(--orange);line-height:1.7}
.contact p:last-child{border-bottom:none}
</style>
</head>
<body>
<main class="canvas">

  <section class="slide col-left row1">
    <div style="position:absolute;left:40px;top:60px;font-size:15px;font-weight:700;color:var(--blue)">Kaltwerk</div>
    <h1 style="position:absolute;left:40px;top:125px;font-size:17px;font-weight:800;color:var(--orange);line-height:1.9">PRESENTATION TITLE<br><span style="color:#fff">GOES HERE</span></h1>
    <p style="position:absolute;left:40px;top:200px;font-size:8px;line-height:1.6;color:var(--text);width:150px">Lorem ipsum dolor sit amet, consectetuer adipiscing elit, sed diam nonummy nibh euis</p>
  </section>

  <section class="slide col-right row1">
    <h2 class="slide-title" style="left:45px;top:30px">About us</h2>
    <div class="brand">Kaltwerk</div>
    <div class="photo gray-photo" role="img" aria-label="Porträt des Beraters im dunklen Anzug" style="left:73px;top:74px;width:174px;height:216px"></div>
    <div role="img" aria-label="Abzeichen" style="position:absolute;left:182px;top:204px;width:30px;height:30px;border-radius:50%;background:#1e1e1e"></div>
    <div class="body" style="left:257px;top:82px;width:240px">
      <h4>Lorem ipsum dolor sit amet</h4>
      <p>Lorem ipsum dolor sit amet, consectetuer adipiscing elit, sed diam nonummy nibh euismod tincidunt ut laoreet dolore magna aliquam erat volutpat. Ut wisi enim ad minim veniam, quis nostrud exerci tation ullamcorper suscipit lobortis nisl ut aliquip ex ea commodo consequat. Duis autem vel eum iriure dolor in hendrerit in vulputate velit esse.</p>
      <p>Lorem ipsum dolor sit amet, consectetuer adipiscing elit, sed diam nonummy nibh euismod tincidunt ut laoreet dolore magna aliquam erat volutpat. Ut wisi enim ad minim veniam, quis nostrud exerci tation ullamcorper suscipit lobortis nisl ut aliquip ex ea commodo consequat. Duis autem vel eum iriure dolor in hendrerit in vulputate velit esse.</p>
    </div>
    <div class="footer-note">© Kaltwerk Presentation, 2024</div>
    <div class="page-no">02</div>
  </section>

  <section class="slide col-left row2">
    <h2 class="slide-title" style="left:45px;top:30px">Page two</h2>
    <div class="brand">Kaltwerk</div>
    <div class="body" style="left:47px;top:82px;width:200px">
      <h4>Lorem ipsum dolor sit amet</h4>
      <p>Lorem ipsum dolor sit amet, consectetuer adipiscing elit, sed diam nonummy nibh euismod tincidunt ut laoreet dolore magna aliquam erat volutpat. Ut wisi enim ad minim veniam, quis nostrud exerci tation ullamcorper suscipit lobortis.</p>
      <h4>Lorem ipsum dolor sit amet</h4>
      <p>Lorem ipsum dolor sit amet, consectetuer adipiscing elit, sed diam nonummy nibh euismod tincidunt ut laoreet dolore magna aliquam erat volutpat. Ut wisi enim ad minim veniam, quis nostrud exerci tation ullamcorper suscipit lobortis.</p>
    </div>
    <div class="body" style="left:280px;top:82px;width:200px">
      <h4>Lorem ipsum dolor sit amet</h4>
      <p>Lorem ipsum dolor sit amet, consectetuer adipiscing elit, sed diam nonummy nibh euismod tincidunt ut laoreet dolore magna aliquam erat volutpat. Ut wisi enim ad minim veniam, quis nostrud exerci tation ullamcorper suscipit lobortis.</p>
      <h4>Lorem ipsum dolor sit amet</h4>
      <p>Lorem ipsum dolor sit amet, consectetuer adipiscing elit, sed diam nonummy nibh euismod tincidunt ut laoreet dolore magna aliquam erat volutpat. Ut wisi enim ad minim veniam, quis nostrud exerci tation ullamcorper suscipit lobortis.</p>
    </div>
    <div class="footer-note">© Kaltwerk Presentation, 2024</div>
    <div class="page-no">03</div>
  </section>

  <section class="slide col-right row2">
    <div class="photo" role="img" aria-label="Laptop und Kaffeetasse auf dunklem Tisch" style="left:280px;top:0;width:239px;height:290px;background:linear-gradient(170deg,#4a4a4a 0%,#2e2e2e 50%,#1c1c1c 100%)"></div>
    <h2 class="slide-title" style="left:45px;top:64px">Page three</h2>
    <div class="brand">Kaltwerk</div>
    <div class="body" style="left:45px;top:106px;width:200px">
      <p>Lorem ipsum dolor sit amet, consectetuer adipiscing elit, sed diam nonummy nibh euismod tincidunt ut laoreet dolore magna aliquam erat volutpat. Ut wisi enim ad minim veniam, quis nostrud exerci tation ullamcorper suscipit lobortis.</p>
      <p>Lorem ipsum dolor sit amet, consectetuer adipiscing elit, sed diam nonummy nibh euismod tincidunt ut laoreet dolore magna aliquam erat volutpat. Ut wisi enim ad minim veniam, quis nostrud exerci tation ullamcorper suscipit lobortis.</p>
    </div>
    <div class="footer-note">© Kaltwerk Presentation, 2024</div>
    <div class="page-no">04</div>
  </section>

  <section class="slide col-left row3">
    <h2 class="slide-title" style="left:170px;top:131px"><span class="accent">Our</span> portfolio</h2>
  </section>

  <section class="slide col-right row3">
    <div class="photo gray-photo" role="img" aria-label="Hochhausfassade in Schwarzweiß" style="left:67px;top:0;width:213px;height:290px"></div>
    <div class="brand">Kaltwerk</div>
    <h2 class="slide-title" style="left:25px;top:125px"><span class="accent">Solution design</span><br>&amp; architecture</h2>
    <div class="body" style="left:295px;top:108px;width:190px">
      <p>Do you feel the need of overarching technical guidance for your DataHarbor platform? Or do you struggle to find experienced solution architects for your projects? Let me help you by providing independent architecture advisory for projects delivered internally or by DataHarbor partners or act as an interim solution architect providing an unbiased support.</p>
    </div>
    <div class="footer-note">© Kaltwerk Presentation, 2024</div>
    <div class="page-no">06</div>
  </section>

  <section class="slide col-left row4">
    <div class="photo gray-photo" role="img" aria-label="Team bei einem Workshop im Büro" style="left:0;top:0;width:272px;height:290px"></div>
    <div class="brand">Kaltwerk</div>
    <h2 class="slide-title" style="left:25px;top:125px"><span class="accent">Platform strategy</span><br>and governance</h2>
    <div class="body" style="left:295px;top:104px;width:190px">
      <p>Are you drowning in daily operations and escalations without a chance to focus on strategic topics? I will help you to develop a long-term strategy and establish a governance structure to allow efficient operation of your DataHarbor platform with an established roadmap, measurable value and a clear decision making process.</p>
    </div>
    <div class="footer-note">© Kaltwerk Presentation, 2024</div>
    <div class="page-no">07</div>
  </section>

  <section class="slide col-right row4">
    <div class="photo" role="img" aria-label="Programmcode auf dunklem Bildschirm" style="left:67px;top:0;width:205px;height:290px;background:linear-gradient(160deg,#3a3a3a 0%,#1c1c1c 60%,#111 100%)"></div>
    <div class="brand">Kaltwerk</div>
    <h2 class="slide-title" style="left:25px;top:125px"><span class="accent">Unified service</span><br><span class="accent">model</span> (USM)</h2>
    <div class="body" style="left:295px;top:104px;width:190px">
      <p>Have you ever wondered what the Unified Service Model (USM) is and how you can benefit from it? I will support you in setting up your business service and offering structure to conform with the USM. This will allow you to effectively measure service levels, take better advantage of the DataHarbor products as well as transparent reporting and service costing.</p>
    </div>
    <div class="footer-note">© Kaltwerk Presentation, 2024</div>
    <div class="page-no">08</div>
  </section>

  <section class="slide light col-left row5">
    <h2 class="slide-title" style="left:168px;top:131px"><span class="accent">Recent</span> project</h2>
  </section>

  <section class="slide light col-right row5">
    <h2 class="slide-title" style="left:170px;top:26px"><span class="accent">Recent</span> project</h2>
    <div class="brand">Kaltwerk</div>
    <div class="cards">
      <article class="card filled">
        <div class="card-head"><svg width="26" height="26" viewBox="0 0 26 26" fill="none" stroke="#e5782a" stroke-width="1.4"><circle cx="13" cy="13" r="10"/><path d="M3 13h20M13 3c4 4 4 16 0 20M13 3c-4 4-4 16 0 20"/></svg>
          <div class="card-title"><span class="accent">SERVICE DESK &amp; USM</span>IMPLEMENTATION<small>Industry: Healthcare</small></div></div>
        <p>Responsibilities: DataHarbor lead architect to develop a target model for the end-to-end customer service processes in ERP and DataHarbor together with the customer's enterprise architects.</p>
        <div class="card-duration">Duration: 9 Months</div>
      </article>
      <article class="card filled">
        <div class="card-head"><svg width="26" height="26" viewBox="0 0 26 26" fill="none" stroke="#e5782a" stroke-width="1.4"><rect x="4" y="6" width="9" height="17"/><rect x="13" y="2" width="9" height="21"/><path d="M7 10h3M7 14h3M16 6h3M16 10h3M16 14h3"/></svg>
          <div class="card-title"><span class="accent">BUILD CENTER OF</span>EXCELLENCE<small>Industry: Automotive</small></div></div>
        <p>Responsibilities: Support in building up the Center of Excellence and introducing a Demand Management process during the split of two global companies. Overall architectural advisory for platform projects in a multi-vendor environment.</p>
        <div class="card-duration">Duration: 12 Months</div>
      </article>
      <article class="card filled">
        <div class="card-head"><svg width="26" height="26" viewBox="0 0 26 26" fill="none" stroke="#e5782a" stroke-width="1.4"><rect x="4" y="5" width="18" height="12"/><path d="M2 20h22"/></svg>
          <div class="card-title"><span class="accent">USM</span>IMPLEMENTATION<small>Industry: Healthcare</small></div></div>
        <p>Responsibilities: Lead Architect for the initial USM implementation, define business services, service offerings and application services in accordance to the Unified Service Model (USM), guidance for the platform roadmap planning.</p>
        <div class="card-duration">Duration: 12 Months</div>
      </article>
    </div>
    <div class="band" style="background:var(--slide)">
      <div class="footer-note">© Kaltwerk Presentation, 2024</div>
      <div class="page-no">10</div>
    </div>
  </section>

  <section class="slide col-left row6">
    <h2 class="slide-title" style="left:170px;top:26px"><span class="accent">Recent</span> project</h2>
    <div class="brand">Kaltwerk</div>
    <div class="cards">
      <article class="card outlined">
        <div class="card-head"><svg width="26" height="26" viewBox="0 0 26 26" fill="none" stroke="#e5782a" stroke-width="1.4"><circle cx="13" cy="13" r="10"/><path d="M3 13h20M13 3c4 4 4 16 0 20M13 3c-4 4-4 16 0 20"/></svg>
          <div class="card-title"><span class="accent">SERVICE DESK &amp; USM</span>IMPLEMENTATION<small>Industry: Healthcare</small></div></div>
        <p>Responsibilities: DataHarbor lead architect to develop a target model for the end-to-end customer service processes in ERP and DataHarbor together with the customer's enterprise architects.</p>
        <div class="card-duration">Duration: 9 Months</div>
      </article>
      <article class="card outlined">
        <div class="card-head"><svg width="26" height="26" viewBox="0 0 26 26" fill="none" stroke="#e5782a" stroke-width="1.4"><rect x="4" y="6" width="9" height="17"/><rect x="13" y="2" width="9" height="21"/><path d="M7 10h3M7 14h3M16 6h3M16 10h3M16 14h3"/></svg>
          <div class="card-title"><span class="accent">BUILD CENTER OF</span>EXCELLENCE<small>Industry: Automotive</small></div></div>
        <p>Responsibilities: Support in building up the Center of Excellence and introducing a Demand Management process during the split of two global companies. Overall architectural advisory for platform projects in a multi-vendor environment.</p>
        <div class="card-duration">Duration: 12 Months</div>
      </article>
      <article class="card outlined">
        <div class="card-head"><svg width="26" height="26" viewBox="0 0 26 26" fill="none" stroke="#e5782a" stroke-width="1.4"><rect x="4" y="5" width="18" height="12"/><path d="M2 20h22"/></svg>
          <div class="card-title"><span class="accent">USM</span>IMPLEMENTATION<small>Industry: Healthcare</small></div></div>
        <p>Responsibilities: Lead Architect for the initial USM implementation, define business services, service offerings and application services in accordance to the Unified Service Model (USM), guidance for the platform roadmap planning.</p>
        <div class="card-duration">Duration: 12 Months</div>
      </article>
    </div>
    <div class="band orange" style="background:var(--orange)">
      <div class="footer-note">© Kaltwerk Presentation, 2024</div>
      <div class="page-no">11</div>
    </div>
  </section>

  <section class="slide col-right row6">
    <h2 class="slide-title" style="left:45px;top:30px;color:var(--orange)">Quote</h2>
    <div class="brand">Kaltwerk</div>
    <div class="quote-mark">“</div>
    <p class="quote-text">We cannot solve problems with the kind of thinking<br>we employed when we came up with them.</p>
    <p class="quote-author">— Clara Wendt</p>
    <div class="body" style="left:56px;top:190px;width:430px">
      <p>Lorem ipsum dolor sit amet, consectetuer adipiscing elit, sed diam nonummy nibh euismod tincidunt ut laoreet dolore magna aliquam erat volutpat. Ut wisi enim ad minim veniam, quis nostrud exerci tation ullamcorper suscipit lobortis nisl ut aliquip ex ea commodo consequat. Duis autem vel eum iriure dolor in hendrerit in vulputate velit esse.</p>
    </div>
    <div class="footer-note">© Kaltwerk Presentation, 2024</div>
    <div class="page-no">12</div>
  </section>

  <section class="slide col-left row7">
    <div class="photo gray-photo" role="img" aria-label="Moderne Gebäudefassade" style="left:39px;top:56px;width:198px;height:174px"></div>
    <div style="position:absolute;left:39px;top:195px;width:198px;height:35px;background:var(--orange);opacity:.85"></div>
    <div class="brand" style="left:50px;right:auto;top:40px">Kaltwerk</div>
    <h2 class="slide-title" style="left:280px;top:30px">Page four</h2>
    <div class="body" style="left:280px;top:82px;width:200px">
      <h4>Lorem ipsum dolor sit amet</h4>
      <p>Lorem ipsum dolor sit amet, consectetuer adipiscing elit, sed diam nonummy nibh euismod tincidunt ut laoreet dolore magna aliquam erat volutpat. Ut wisi enim ad minim veniam, quis nostrud exerci tation ullamcorper suscipit lobortis.</p>
      <h4>Lorem ipsum dolor sit amet</h4>
      <p>Lorem ipsum dolor sit amet, consectetuer adipiscing elit, sed diam nonummy nibh euismod tincidunt ut laoreet dolore magna aliquam erat volutpat. Ut wisi enim ad minim veniam, quis nostrud exerci tation ullamcorper suscipit lobortis.</p>
    </div>
    <div class="footer-note">© Kaltwerk Presentation, 2024</div>
    <div class="page-no">13</div>
  </section>

  <section class="slide col-right row7">
    <div class="photo" role="img" aria-label="Person arbeitet am Laptop" style="left:0;top:0;width:519px;height:140px;background:linear-gradient(180deg,#4c4c4c 0%,#353535 100%)"></div>
    <div class="brand">Kaltwerk</div>
    <h2 class="slide-title" style="left:35px;top:166px">Page five</h2>
    <div class="body" style="left:215px;top:160px;width:275px">
      <h4>Lorem ipsum dolor sit amet</h4>
      <p>Lorem ipsum dolor sit amet, consectetuer adipiscing elit, sed diam nonummy nibh euismod tincidunt ut laoreet dolore magna aliquam erat volutpat. Ut wisi enim ad minim veniam, quis nostrud exerci tation ullamcorper suscipit lobortis. Lorem ipsum dolor sit amet, consectetuer adipiscing elit, sed diam nonummy nibh euismod tincidunt.</p>
    </div>
    <div class="footer-note">© Kaltwerk Presentation, 2024</div>
    <div class="page-no">14</div>
  </section>

  <section class="slide col-left row8">
    <h2 class="slide-title" style="left:45px;top:30px">Page six</h2>
    <div class="brand">Kaltwerk</div>
    <div class="body" style="left:47px;top:76px;width:425px">
      <p>Lorem ipsum dolor sit amet, consectetuer adipiscing elit, sed diam nonummy nibh euismod tincidunt ut laoreet dolore magna aliquam erat volutpat. Ut wisi enim ad minim veniam, quis nostrud exerci tation ullamcorper suscipit lobortis nisl ut aliquip ex ea commodo consequat. Duis autem vel eum iriure dolor in hendrerit in vulputate velit esse molestie consequat, vel illum dolore eu feugiat nulla facilisis at vero eros et accumsan et iusto odio dignissim qui blandit praesent luptatum zzril delenit augue duis dolore te feugait nulla facilisi. Lorem ipsum dolor sit amet, consectetuer adipiscing elit, sed diam nonummy nibh euismod tincidunt ut laoreet dolore magna aliquam erat volutpat. Ut wisi enim ad minim veniam, quis nostrud exerci tation ullamcorper suscipit lobortis nisl ut aliquip ex ea commodo consequat. Lorem ipsum dolor sit amet, consectetuer adipiscing elit, sed diam nonummy nibh euismod tincidunt ut laoreet dolore magna aliquam erat volutpat. Ut wisi enim ad minim veniam, quis nostrud exerci tation ullamcorper suscipit lobortis nisl ut aliquip ex ea commodo consequat. Duis autem vel eum iriure dolor in hendrerit in vulputate velit esse molestie consequat, vel illum dolore eu feugiat nulla facilisis at vero eros et accumsan et iusto odio dignissim. Lorem ipsum dolor sit amet, consectetuer adipiscing elit, sed diam nonummy nibh euismod tincidunt ut laoreet dolore magna aliquam erat volutpat.</p>
    </div>
    <div class="footer-note">© Kaltwerk Presentation, 2024</div>
    <div class="page-no">15</div>
  </section>

  <section class="slide col-right row8">
    <h2 class="slide-title" style="left:170px;top:26px"><span class="accent">Any</span> question?</h2>
    <div class="brand">Kaltwerk</div>
    <div class="contact">
      <p>Lindenweg 7 55118<br>Mainz, Germany</p>
      <p>(+49) 151 234 56 789</p>
      <p>jonas@kaltwerk.de</p>
      <p>www.kaltwerk.de</p>
    </div>
  </section>

</main>
</body>
</html>
```